Brenton Civil

We need a Standard Professional Company Letterhead, company standard document template, coversheet template for a civil construction company. We would like the designs to use the company colour red

I have attached existing templates that need to improve greatly but please use as a quide of general layout.

```html
<!DOCTYPE html>
<html lang="en">
<head>
<meta charset="utf-8">
<title>Brenton Civil Letterhead</title>
<link href="https://fonts.googleapis.com/css2?family=Marcellus&family=Roboto+Condensed:wght@300&family=PT+Sans:wght@400;700&display=swap" rel="stylesheet">
<style>
:root{
  --red:#c3202c;
  --blue:#2b4d86;
  --navy:#1d3561;
  --text:#7a7a7a;
  --ink:#333;
  --paper:#fff;
  --faint:#f1f1f1;
}
*{margin:0;padding:0;box-sizing:border-box}
html,body{width:900px;height:1200px;overflow:hidden;background:var(--paper)}
.letterhead{position:relative;width:900px;height:1200px;background:var(--paper);overflow:hidden}
.edge-tab{position:absolute;width:9px;height:60px}
.edge-tab.red{background:linear-gradient(180deg,#e0303b,var(--red))}
.edge-tab.blue{background:linear-gradient(180deg,#4a74b8,var(--navy))}
.edge-tab.left{left:0}.edge-tab.right{right:0}
.edge-tab.top{top:24px}.edge-tab.lower{top:93px}

.brand{position:absolute;left:333px;top:44px;display:flex;align-items:center;gap:16px}
.brand-dot{width:90px;height:90px;border-radius:50%;background:var(--red)}
.brand-name{font-family:"Marcellus",serif;color:var(--red);font-size:26px;line-height:1.05;letter-spacing:.5px}
.brand-name small{display:block;font-size:19px}

.backdrop-circle{position:absolute;left:234px;top:452px;width:430px;height:430px;border-radius:50%;background:var(--faint)}

.letter-body{position:absolute;left:101px;top:265px;width:698px;font-family:"Roboto Condensed",sans-serif;font-weight:300;font-size:17.6px;letter-spacing:.2px;line-height:26.1px;color:var(--text);hyphens:auto;-webkit-hyphens:auto}
.letter-body p{margin-bottom:26px}
.letter-body p.closing{margin-top:27px}

.signature{position:absolute;left:481px;top:935px;width:300px;height:55px;background:linear-gradient(90deg,#f4f4f4,#ececec,#f4f4f4);border-radius:4px}

.program{position:absolute;left:0;width:900px;top:1068px;text-align:center}
.program-mark{display:inline-flex;align-items:center;gap:10px;font-family:"PT Sans",sans-serif;font-weight:700;font-size:26px;line-height:1;color:var(--red);letter-spacing:.5px}
.program-mark i{width:40px;height:40px;border-radius:50%;background:var(--red);display:inline-block}
.program-tag{font-family:"PT Sans",sans-serif;font-weight:700;font-size:9px;color:#111;margin-top:8px}
.program-rule{position:absolute;left:296px;top:1146px;width:300px;height:1px;background:linear-gradient(90deg,transparent,var(--red),transparent)}

.contact{position:absolute;left:0;width:900px;top:1152px;display:flex;justify-content:center;gap:6px;font-family:"PT Sans",sans-serif;font-size:13.3px;font-style:normal;color:#444}
.contact span{display:inline-flex;align-items:center;gap:4px}
.contact svg{width:13px;height:13px}

.footer-bands{position:absolute;left:0;bottom:0;width:900px;height:27px}
</style>
</head>
<body>
<main class="letterhead">
  <div class="edge-tab red left top"></div>
  <div class="edge-tab blue left lower"></div>
  <div class="edge-tab red right top"></div>
  <div class="edge-tab blue right lower"></div>

  <header class="brand">
    <div class="brand-dot"></div>
    <div class="brand-name">BRENTON<small>CIVIL PTY LTD</small></div>
  </header>

  <div class="backdrop-circle"></div>

  <section class="letter-body">
    <p>Lorem Ipsum is simply dummy text of the printing and typesetting industry. Lorem Ipsum has been the industry’s standard dummy text ever since the 1500s, when an unknown printer took a galley of type and scrambled it to make a type specimen book. It has survived not only five centuries, but also the leap into electronic typesetting, remaining essentially unchanged. It was popularised in the 1960s with the release of Typeset sheets containing Lorem Ipsum passages, and more recently with desktop publishing software like Folio Layout including versions of Lorem Ipsum.</p>
    <p>It is a long established fact that a reader will be distracted by the readable content of a page when looking at its layout. The point of using Lorem Ipsum is that it has a more-or-less normal distribution of letters, as opposed to using ’Content here, content here’, making it look like readable English. Many desktop publishing packages and web page editors now use Lorem Ipsum as their default model text, and a search for ’lorem ipsum’ will uncover many web sites still in their infancy. Various versions have evolved over the years, sometimes by accident, sometimes on purpose (injected humour and the like).</p>
    <p class="closing">Contrary to popular belief, Lorem Ipsum is not simply random text. It has roots in a piece of classical Latin literature from 45 BC, making it over 2000 years old. Daniel Ashcombe, a Latin professor at Whitfield College in Vermont, looked up one of the more obscure Latin words, consectetur, from a Lorem Ipsum passage, and going through the cites of the word in classical literature, discovered the undoubtable source. Lorem Ipsum comes from sections 1.10.32 and 1.10.33 of "de Finibus Bonorum et Malorum" structures, to generate Lorem Ipsum which looks reasonable. The generated Lorem Ipsum is therefore always free from repetition, injected humour, or non-characteristic words etc.</p>
  </section>

  <div class="signature" role="img" aria-label="Handwritten signature of the sender"></div>

  <div class="program">
    <div class="program-mark"><i></i>SAFEBUILD</div>
    <div class="program-tag">Site Care Pledge for Every Crew</div>
  </div>
  <div class="program-rule"></div>

  <address class="contact">
    <span><svg viewBox="0 0 16 16"><circle cx="8" cy="8" r="7" fill="none" stroke="#c3202c" stroke-width="1.4"/><path d="M8 3.5a2.8 2.8 0 0 0-2.8 2.8C5.2 8.6 8 12 8 12s2.8-3.4 2.8-5.7A2.8 2.8 0 0 0 8 3.5z" fill="#c3202c"/></svg>PO Box 52, Moranbah Qld 4744</span>
    <span><svg viewBox="0 0 16 16"><circle cx="8" cy="8" r="7" fill="none" stroke="#333" stroke-width="1.2"/><path d="M5.2 4.3l1.5-.3.8 2-1 .8a5 5 0 0 0 2.5 2.5l.8-1 2 .8-.3 1.5c-3.5.3-6.6-2.8-6.3-6.3z" fill="#333"/></svg>0400 318 276</span>
    <span><svg viewBox="0 0 16 16"><circle cx="8" cy="8" r="7.5" fill="#c3202c"/><rect x="4" y="5.3" width="8" height="5.4" fill="none" stroke="#fff" stroke-width="1"/><path d="M4 5.5l4 3 4-3" fill="none" stroke="#fff" stroke-width="1"/></svg>info@brentoncivil.com.au</span>
    <span><svg viewBox="0 0 16 16"><circle cx="8" cy="8" r="7" fill="none" stroke="#c3202c" stroke-width="1.4"/><circle cx="8" cy="8" r="4" fill="#c3202c"/></svg>ABN 12 405 731 669</span>
  </address>

  <svg class="footer-bands" viewBox="0 0 900 27" preserveAspectRatio="none">
    <rect x="0" y="0" width="900" height="3" fill="var(--navy)"/>
    <polygon points="0,5 265,5 260,9 0,9" fill="var(--blue)"/>
    <polygon points="272,5 592,5 586,9 266,9" fill="var(--red)"/>
    <polygon points="598,5 900,5 900,9 592,9" fill="var(--blue)"/>
    <rect x="0" y="12" width="690" height="15" fill="var(--blue)"/>
    <rect x="690" y="12" width="210" height="15" fill="var(--red)"/>
  </svg>
</main>
</body>
</html>
```